KelvoSHIELD Brochure

We need a new brochure designed for our KelvoSHIELD Unit. I have provided examples of previous and words for the new ones. Stock photos will be purchased and forwarded once design is complete.

I have also attached a competitors product brochure for reference. This is a bout conveying by using our product your people will be safe and will not need to use high rated PPE
Updates

Project Deadline Extended
Reason: Will be extending the project for 1 day and selecting the final design tomorrow to allow some of you to fine tune submissions.

Target Market(s)

Professionals

Industry/Entity Type

Product

Contact Information for Business Card

Refer Attached Details

Requirements
Must have
• Brantley Osgood Logo and Colours Business Card
• Brochure should complement KelvoSHIELD Logo

```html
<!DOCTYPE html>
<html lang="en">
<head>
<meta charset="utf-8">
<title>KelvoSHIELD Brochure Spread</title>
<link href="https://fonts.googleapis.com/css2?family=Lato:wght@400;700;900&family=Arimo:wght@400;700&display=swap" rel="stylesheet">
<style>
  :root {
    --backdrop: #e4e2df;
    --paper: #ffffff;
    --paper-shade: #e3e6ec;
    --accent-red: #cc1f3e;
    --accent-blue: #1f5f95;
    --ink: #2b2b2f;
    --flash-tint: rgba(204, 31, 62, 0.07);
    --photo-steel-a: #cfd6dc;
    --photo-steel-b: #8c98a4;
    --photo-site-a: #d9dde0;
    --photo-site-b: #d86a2c;
  }
  * { box-sizing: border-box; margin: 0; padding: 0; }
  html, body { width: 1200px; height: 753px; overflow: hidden; }
  body {
    background: var(--backdrop);
    font-family: "Arimo", Arial, sans-serif;
    color: var(--ink);
  }
  .spread {
    position: absolute;
    left: 40px; top: 26px;
    width: 1120px; height: 700px;
    display: flex;
    box-shadow: 0 6px 24px rgba(0,0,0,0.18);
  }
  .page {
    position: relative;
    width: 560px; height: 700px;
    overflow: hidden;
  }
  .page--left {
    background: linear-gradient(180deg, var(--paper) 0%, var(--paper-shade) 100%);
    padding: 44px 38px 30px 40px;
  }
  .page--right {
    background: linear-gradient(180deg, var(--paper-shade) 0%, var(--paper) 40%, var(--paper-shade) 100%);
  }
  .flash-decor {
    position: absolute;
    left: 90px; top: 150px;
    width: 300px; height: 520px;
    background: radial-gradient(ellipse at center, var(--flash-tint) 0%, rgba(204,31,62,0) 70%);
  }
  .content { position: relative; }
  .section-title {
    font-family: "Lato", Arial, sans-serif;
    font-weight: 700;
    color: var(--accent-red);
    font-size: 17px;
    line-height: 1.2;
    margin: 12px 0 4px;
  }
  .section-title:first-child { margin-top: 0; }
  .section-title--large { font-size: 19px; }
  .body-text { font-size: 10.5px; line-height: 1.3; }
  .body-text--justify { text-align: justify; }
  .bullet-list, .number-list { font-size: 10.5px; line-height: 1.3; padding-left: 26px; margin: 6px 0; }
  .number-list { padding-left: 30px; margin: 2px 0; }
  .hero-photo {
    height: 190px;
    background: linear-gradient(100deg, var(--photo-steel-a) 0%, var(--photo-steel-b) 55%, var(--photo-steel-a) 100%);
  }
  .hero-band { height: 8px; background: var(--accent-blue); }
  .right-content { padding: 22px 30px 0 30px; }
  .benefits {
    display: flex;
    gap: 14px;
    margin-top: 4px;
  }
  .benefit-list { list-style: none; width: 290px; }
  .benefit-item {
    display: flex;
    gap: 12px;
    font-size: 10.5px;
    line-height: 1.3;
    margin-bottom: 9px;
  }
  .benefit-number {
    flex: none;
    width: 18px; height: 16px;
    background: var(--accent-blue);
    color: #fff;
    font-family: "Lato", Arial, sans-serif;
    font-weight: 700;
    font-size: 9px;
    display: flex; align-items: center; justify-content: center;
    margin-top: 4px;
  }
  .benefit-item strong { font-weight: 700; }
  .site-photo {
    flex: none;
    width: 226px; height: 270px;
    margin-top: -40px;
    margin-right: -30px;
    background: linear-gradient(160deg, var(--photo-site-a) 0%, var(--photo-site-a) 30%, var(--photo-site-b) 60%, #9aa0a4 100%);
  }
</style>
</head>
<body>
  <main class="spread">
    <section class="page page--left">
      <div class="flash-decor" role="img" aria-label="Faint red arc flash graphic behind the text"></div>
      <div class="content">
        <h2 class="section-title">The Arc Flash Problem</h2>
        <p class="body-text">Electrical safety generally has been geared towards preventing electrocution with statistics indication industry has been successful in achieving. Arc Flash is NOT an Electric Shock; it is an ELECTRICAL PLASMA EXPLOSION which is capable of severely burning personnel within the exposure area.</p>
        <p class="body-text">The explosion can maim or kill within as little time as 40ms by expelling outwards from the source:</p>
        <ul class="bullet-list">
          <li>Extreme Temperatures;</li>
          <li>Molten Metal;</li>
          <li>Toxic Gases</li>
          <li>High Pressure Wave</li>
        </ul>

        <h2 class="section-title">The Hazards again are:</h2>
        <ul class="bullet-list">
          <li>Heat causes 2<sup>nd</sup> degree burns on exposed skin;</li>
          <li>Heat ignites clothing causing severe 3<sup>rd</sup> degree burns;</li>
          <li>Inhaling of molten metal and the toxic plasma plume causes lung damage;</li>
          <li>Pressure wave sound can exceed levels which can damage human ears;</li>
          <li>Pressure wave can cause personnel injury.</li>
        </ul>

        <h2 class="section-title">The Complacency Problem</h2>
        <p class="body-text body-text--justify">How often have you heard, this has never happen in our facility our processes and equipment very good and will prevent this? This is a game of bravado and probability as most arc flash events are caused by:</p>
        <ol class="number-list">
          <li>Human error.</li>
          <li>Equipment failure;</li>
          <li>Vermin Infestation.</li>
        </ol>
        <p class="body-text">Can you truly place your hand on your heart and say these events will never happens at your facility?</p>

        <h2 class="section-title section-title--large">What are the Severity Factors Involved?</h2>
        <p class="body-text">The severity factors involved are:</p>
        <ol class="number-list">
          <li>Energy, how big is the explosion;</li>
          <li>Time, how long does the explosion go for;</li>
          <li>Distance, how close to the explosion will I be.</li>
        </ol>
        <p class="body-text">The most effective way lowing the severity of an Arc Flash Event is to reduce Energy Quickly.</p>

        <h2 class="section-title section-title--large">Why Not Just Use Rate PPE</h2>
        <p class="body-text body-text--justify">Providing separation and distance via PPE should be your last choice to manage this problem. Don't let the judicial system judge whether your PPE was adequate risk prevention in the event of an incident. Courts often take the view that irrespective of the numerical risk criteria, the broad aim should be to avoid risk So Far As Is Reasonably Practical (SFAIRF).</p>
      </div>
    </section>

    <section class="page page--right">
      <div class="hero-photo" role="img" aria-label="Photo of a switchgear room with rows of electrical panels"></div>
      <div class="hero-band"></div>
      <div class="right-content">
        <h2 class="section-title">What is our Solution?</h2>
        <p class="body-text">Our simple but elegant engineered high speed fuse assembly installed on the secondary (480V) side of distribution transformers. The assembly is engineered to carry normal load currents up to 3600A, but respond extremely quickly to fault currents interrupting faults within half cycle (5ms@50Hz/4ms@60Hz) and limiting arc incident energy to less than 1.2 cal\cm2.</p>

        <h2 class="section-title">Significant Benefits Include</h2>
        <div class="benefits">
          <ol class="benefit-list">
            <li class="benefit-item"><span class="benefit-number">1</span><span>Protects personnel from severe burns by reducing the Arc Flash Incident Energy to less than 1.2 cal\cm2 in 415/480V systems = <strong>Safer Work Environment;</strong></span></li>
            <li class="benefit-item"><span class="benefit-number">2</span><span>Enables personnel to operated 480V electrical equipment with PEE rated for less than 4 cal\cm2. = <strong>More wearable and comfortable PPE clothing;</strong></span></li>
            <li class="benefit-item"><span class="benefit-number">3</span><span>Low capital cost compared to equipment replacement. = <strong>Efficient use of Scarce Capital;</strong></span></li>
            <li class="benefit-item"><span class="benefit-number">4</span><span>Can be retrofitted to any installation within 16-24 hrs.= Low Production Impact to Implement;</span></li>
            <li class="benefit-item"><span class="benefit-number">5</span><span>Rigorously tested at an internationally recognized VKT test facility. = <strong>Guaranteed to Work in our certified engineered applications;</strong></span></li>
            <li class="benefit-item"><span class="benefit-number">6</span><span>System uniquely protects at the source of the energy. = <strong>Safer, Protected Assets;</strong></span></li>
            <li class="benefit-item"><span class="benefit-number">7</span><span>When it is required to operate, you will be up and running within hours not days or months = <strong>Low Production Impact from Arc Flash Safety Incident</strong></span></li>
          </ol>
          <div class="site-photo" role="img" aria-label="Photo of an orange protection unit installed beside a transformer in a fenced yard"></div>
        </div>
      </div>
    </section>
  </main>
</body>
</html>
```